Multinational, Mobile Telecommunications Software Solution provider needing a powerful banner for Jo

We need a banner ad design for our company "Corvane Systems"
We provide innovative, customer-centric IT solutions to mobile / cellular telecommunications service providers. We empower service providers with highly customizable solutions that can be seamlessly integrated into the existing business processes, and a variety of turnkey solutions that will help optimize business. We have branches in Asia, Africa, Middle East and Europe and currently employ staff of 23 nationalities. We strive to be the employer of choice. We need to communicate a strong people-centric and diverse culture. Our corporate colour is blue - attached is our logo.

Industry/Entity Type

It Company

```html
<!DOCTYPE html>
<html lang="en">
<head>
<meta charset="utf-8">
<title>Corvane Systems – Telecom Solutions Banner</title>
<link rel="stylesheet" href="https://fonts.googleapis.com/css2?family=PT+Sans:ital,wght@0,400;1,400&display=swap">
<style>
  :root {
    --canvas-grey: #d3d6d8;
    --deep-teal: #2e5668;
    --mid-teal: #5d8293;
    --soft-teal: #93aebb;
    --pale-grey: #e9ebec;
    --light-grey: #c4c8cb;
    --text-white: #ffffff;
    --tower-sky: #7f9fb8;
    --tower-steel: #c9ccc9;
    --device-dark: #2b2d30;
    --device-mid: #5b5e62;
  }

  html, body {
    margin: 0;
    padding: 0;
    width: 1200px;
    height: 425px;
    overflow: hidden;
    background: var(--canvas-grey);
  }

  .banner {
    position: relative;
    width: 1200px;
    height: 425px;
    overflow: hidden;
    font-family: "PT Sans", "Helvetica Neue", Arial, sans-serif;
    color: var(--text-white);
  }

  .banner__backdrop {
    position: absolute;
    inset: 0;
    width: 1200px;
    height: 425px;
  }

  .banner__copy {
    position: absolute;
    left: 390px;
    top: 38px;
  }

  .banner__headline {
    margin: 0;
    font-weight: 400;
    font-size: 38px;
    line-height: 47px;
    letter-spacing: -0.3px;
    text-shadow: 0 1px 2px rgba(20, 40, 50, 0.25);
  }

  .banner__services {
    list-style: none;
    margin: 24px 0 0 0;
    padding: 0;
    font-style: italic;
    font-size: 18px;
    line-height: 29px;
  }

  .banner__more {
    display: inline-block;
    margin: 20px 0 0 8px;
    font-style: italic;
    font-size: 18px;
    color: var(--text-white);
    text-decoration: none;
  }
</style>
</head>
<body>
  <section class="banner">
    <svg class="banner__backdrop" viewBox="0 0 1200 425" xmlns="http://www.w3.org/2000/svg">
      <defs>
        <linearGradient id="sweep-deep" x1="0" y1="0" x2="1" y2="1">
          <stop offset="0" stop-color="var(--deep-teal)"/>
          <stop offset="0.55" stop-color="var(--mid-teal)"/>
          <stop offset="1" stop-color="var(--soft-teal)"/>
        </linearGradient>
        <linearGradient id="sweep-light" x1="0" y1="0" x2="1" y2="0">
          <stop offset="0" stop-color="var(--pale-grey)"/>
          <stop offset="1" stop-color="var(--light-grey)"/>
        </linearGradient>
        <linearGradient id="tower-tones" x1="0" y1="0" x2="0" y2="1">
          <stop offset="0" stop-color="var(--tower-sky)"/>
          <stop offset="0.6" stop-color="var(--tower-steel)"/>
          <stop offset="1" stop-color="#8d9396"/>
        </linearGradient>
        <linearGradient id="device-tones" x1="0" y1="0" x2="1" y2="1">
          <stop offset="0" stop-color="var(--device-mid)"/>
          <stop offset="0.5" stop-color="var(--device-dark)"/>
          <stop offset="1" stop-color="#1c1d1f"/>
        </linearGradient>
        <linearGradient id="device-reflection" x1="0" y1="0" x2="0" y2="1">
          <stop offset="0" stop-color="#6a6d70" stop-opacity="0.45"/>
          <stop offset="1" stop-color="#6a6d70" stop-opacity="0"/>
        </linearGradient>
      </defs>

      <!-- base light field -->
      <rect width="1200" height="425" fill="url(#sweep-light)"/>

      <!-- deep blue sweep behind the headline -->
      <path d="M170 0 L1120 0 C1010 70 900 115 790 150 C690 185 640 260 660 425 L300 425 C250 300 215 150 170 0 Z"
            fill="url(#sweep-deep)"/>

      <!-- soft lighter ribbon through the middle -->
      <path d="M380 425 C420 330 520 260 680 230 C820 205 960 190 1200 120 L1200 170 C980 240 820 260 700 290 C600 320 560 370 560 425 Z"
            fill="var(--soft-teal)" opacity="0.45"/>

      <!-- light curve in the lower left -->
      <path d="M0 300 C120 360 260 370 380 425 L0 425 Z" fill="var(--pale-grey)"/>

      <!-- tower image area -->
      <path d="M0 0 L205 0 C250 110 280 230 290 330 C230 375 120 385 60 350 C20 320 0 250 0 200 Z"
            fill="url(#tower-tones)" role="img" aria-label="Telecom transmission tower with microwave dish antennas"/>

      <!-- handset image area -->
      <path d="M820 190 L1150 145 C1175 142 1188 158 1188 180 L1188 330 C1188 352 1175 362 1155 364 L850 395 C830 397 815 385 812 365 L800 220 C798 204 806 192 820 190 Z"
            fill="url(#device-tones)" role="img" aria-label="Slide-out smartphone with touchscreen and keyboard"/>
      <path d="M812 398 L1188 366 L1188 425 L830 425 Z" fill="url(#device-reflection)"/>
    </svg>

    <div class="banner__copy">
      <h1 class="banner__headline">Corvane Systems is focusing on<br>solutions for Telecom operators<br>to provide better services</h1>
      <ul class="banner__services">
        <li>- Project On Demand and Consulting</li>
        <li>- Project Management and Integration</li>
        <li>- Hotline and Support</li>
      </ul>
      <a class="banner__more" href="#">read more &gt;&gt;</a>
    </div>
  </section>
</body>
</html>
```